【サイトマップ・ワイヤーフレーム】
「補足説明」より各種データをDLの上、ご参照ください。

【デザインカラー】
暖色系 / 茶系 / 緑系
※現サイトの緑はあまり好きではないです。
※全体的にあたたかみが出るような色使いでお願いします。

【デザインテイスト】
①ナチュラル
②優しい
③知性的
https://hinatanomori-kissa.com/
1ページ
茶系、緑系、黄・オレンジ系
【素材】
①サイトマップ・ワイヤーフレーム
以下URLよりDLお願いいたします。
http://kumobako.jp/download/3a7c2e91d04b6f85a1e9c37d20b84f6e1a5d9c02
pw:pass

②写真(店内外観)
以下URLよりDLお願いいたします。
http://kumobako.jp/download/7d18f4a2c96e0b35e8a4f71c2d9b60a5e3c81f47
pw:pass

③写真(その他)
ピクモル[ https://jp.pikumoru.com/ ]で定期契約をしています。
クレジット購入のみのもの以外をご利用下さい。
また定期契約のものは弊社の負担となり、ランサー様に負担はありません。
カンプ画像を入れてください。
■店舗写真
http://kumobako.jp/download/b25e9c10f7a43d86c1e2a0f97b4d3c58e6a71d29
pw:pass
※補足説明内のURLが間違っておりました。大変失礼いたしました。
この度多くのデザインを見てみたい為、
1週間延長させて頂きます。
ご応募お待ちしております。
この度多くのデザインを見てみたい為、
1週間延長させて頂きます。
ご応募お待ちしております。
この度は様々なデザインをご提案いただいており、誠に有難う御座います。
こちら都合で大変恐縮ですが、選定期限を【2018/12/31】まで延長させていただいております。
各デザイナー様にはお時間を頂戴し申し訳ございませんが、引き続きどうぞよろしくお願いいたします。

全体的なデザイン性が気に入りました。

この度は皆様良いデザインをご提案いただきありがとうございました。
また何かございましたらご協力お願いいたします。

```html
<!DOCTYPE html>
<html lang="ja">
<head>
<meta charset="utf-8">
<title>ひだまり整骨院</title>
<link href="https://fonts.googleapis.com/css2?family=Noto+Sans+JP:wght@400;500;700&family=Noto+Serif+JP:wght@500;700&display=swap" rel="stylesheet">
<style>
:root{
  --orange:#ef9a5a;
  --orange-dark:#e07f3c;
  --peach:#fcebdd;
  --peach-light:#fdf5ee;
  --brown:#6b4a36;
  --text:#4a3a30;
  --muted:#9a8a7e;
  --line:#ead9cb;
  --green:#4caf50;
  --blue:#3b6fb6;
  --red:#d9483b;
  --white:#fff;
}
*{box-sizing:border-box;margin:0;padding:0}
html,body{width:1200px;height:4784px;overflow:hidden}
body{position:relative;background:var(--white);color:var(--text);font-family:"Noto Sans JP",sans-serif;font-size:15px;line-height:1.6}
.abs{position:absolute}

/* header */
.site-header{left:0;top:0;width:1200px;height:140px}
.header-note{left:140px;top:14px;font-size:12px;color:var(--muted);width:620px;line-height:1.5}
.brand{left:140px;top:62px;display:flex;align-items:center;gap:14px}
.brand-mark{width:48px;height:48px;border-radius:50%;background:var(--orange);flex:none}
.brand-name{font-family:"Noto Serif JP",serif;font-weight:700;font-size:32px;color:var(--brown);white-space:nowrap}
.header-tel{right:140px;top:26px;text-align:right}
.header-tel small{display:block;font-size:12px;color:var(--muted)}
.header-tel b{font-size:44px;color:var(--orange-dark);letter-spacing:1px;display:flex;align-items:center;gap:8px;line-height:1.3}
.main-nav{left:0;top:140px;width:1200px;height:52px;background:var(--peach-light);border-top:1px solid var(--line);border-bottom:2px solid var(--orange);display:flex;justify-content:center}
.main-nav a{width:115px;text-align:center;line-height:49px;font-size:13px;color:var(--brown);text-decoration:none;border-left:1px solid var(--line);white-space:nowrap}
.main-nav a:last-child{border-right:1px solid var(--line)}

/* hero */
.hero{left:0;top:192px;width:1200px;height:510px;background:linear-gradient(90deg,#f7e6d8,#efd4bf 55%,#d7b49a)}
.hero-copy{left:140px;top:60px;font-family:"Noto Serif JP",serif;font-weight:700;color:var(--brown);line-height:1.4}
.hero-copy .l1{font-size:46px}
.hero-copy .l2{font-size:54px;color:var(--orange-dark)}
.hero-copy .l3{font-size:54px}
.hero-sub{left:140px;top:300px;font-size:18px;color:var(--brown);background:rgba(255,255,255,.75);padding:4px 14px}
.hero-badges{left:170px;top:362px;display:flex;gap:22px}
.hero-badges span{width:104px;height:104px;border-radius:50%;background:var(--orange);color:#fff;font-size:15px;font-weight:700;display:flex;align-items:center;justify-content:center;text-align:center;line-height:1.3;border:3px solid #fff}
.hero-badges span.alt{background:var(--orange-dark)}

/* sidebar */
.sidebar{left:140px;top:740px;width:260px}
.side-line{background:var(--green);color:#fff;padding:16px;text-align:center;margin-bottom:18px}
.side-line p{font-size:13px}
.side-line b{font-size:32px;display:block;line-height:1.2}
.side-line small{display:block;background:#fff;color:var(--green);font-size:11px;margin-top:8px;padding:3px}
.side-rank{border:1px solid var(--line);padding:14px;margin-bottom:18px}
.side-rank p{font-size:12px;color:var(--muted)}
.side-rank .name{background:var(--red);color:#fff;font-weight:700;font-size:28px;text-align:center;margin:8px 0}
.side-rank .sub{font-size:13px;color:var(--text)}
.side-rank .no1{font-size:26px;font-weight:700;color:var(--red)}
.review{border:1px solid var(--line);padding:10px 12px;margin-bottom:12px;font-size:12px;line-height:1.55}
.review .stars{color:var(--orange);font-size:14px;letter-spacing:2px}
.review .who{color:var(--muted);margin-top:4px}
.side-btn{background:var(--orange-dark);color:#fff;text-align:center;font-size:14px;padding:10px;margin:6px 0 18px}
.banner{height:74px;margin-bottom:12px;display:flex;align-items:center;justify-content:center;font-weight:700;font-size:22px;color:#fff}
.banner.b1{background:var(--blue)}
.banner.b2{background:var(--red)}
.banner.b3{background:#fff;border:2px solid var(--line);color:var(--brown)}
.side-video{height:180px;background:linear-gradient(#8d7765,#5c4a3e);margin:18px 0 10px}
.side-clinic{height:100px;background:linear-gradient(90deg,#c9a98c,#e6d3c2)}

/* main column */
.main{left:420px;width:640px}
.rank-banner{top:712px;height:72px;background:var(--peach);border:1px solid var(--line);display:flex;align-items:center;padding:0 18px;gap:14px}
.rank-banner .site{background:var(--red);color:#fff;font-weight:700;font-size:20px;padding:4px 10px}
.rank-banner .title{font-size:26px;font-weight:700;color:var(--orange-dark);font-family:"Noto Serif JP",serif}
.rank-banner .first{margin-left:auto;background:var(--orange);color:#fff;font-weight:700;font-size:24px;padding:4px 16px;border-radius:4px}

.sec-title{display:flex;align-items:center;justify-content:center;gap:10px;font-family:"Noto Serif JP",serif;font-weight:700;font-size:28px;color:var(--brown);height:60px;border-bottom:1px dashed var(--line)}
.sec-title::before{content:"";width:14px;height:14px;border-radius:50%;background:var(--orange)}

.worry-grid{top:890px;display:grid;grid-template-columns:repeat(3,1fr);gap:16px}
.worry{height:222px;border:1px solid var(--line);background:#fff}
.worry .pic{height:120px;background:linear-gradient(135deg,#f8e3d1,#e9c4a6);display:flex;align-items:center;padding-left:12px}
.worry .pic b{font-family:"Noto Serif JP",serif;font-size:24px;color:var(--orange-dark);background:rgba(255,255,255,.75);padding:2px 10px;line-height:1.25}
.worry p{font-size:12px;padding:10px 12px;line-height:1.6}

.reason-list{top:1540px}
.reason{display:flex;gap:20px;height:174px;padding:12px 0;border-bottom:1px solid var(--line)}
.reason .pic{width:200px;height:150px;background:linear-gradient(135deg,#e8d6c6,#b99a82);flex:none}
.reason .num{font-family:"Noto Serif JP",serif;font-size:38px;color:var(--orange);line-height:1;font-weight:700}
.reason h3{font-size:19px;color:var(--orange-dark);line-height:1.35;margin:4px 0 6px}
.reason p{font-size:12px;line-height:1.6}

.greeting{top:2400px;display:flex;gap:20px}
.greeting .pic{width:220px;height:220px;background:linear-gradient(#d7c2ae,#8c735f);flex:none}
.greeting p{font-size:13px;line-height:1.7}
.greeting .sign{margin-top:8px;text-align:right;font-family:"Noto Serif JP",serif;font-size:17px;color:var(--brown)}
.photo-strip{top:2650px;height:80px;display:grid;grid-template-columns:repeat(4,1fr);gap:10px}
.photo-strip div{background:linear-gradient(135deg,#e8d2bd,#c3a085)}

.access{top:2770px;height:290px;display:flex;gap:20px}
.access-info{flex:1}
.access-info .logo{display:flex;align-items:center;gap:12px;border-bottom:2px solid var(--orange);padding-bottom:8px;margin-bottom:10px}
.access-info .logo span{width:32px;height:32px;border-radius:50%;background:var(--orange)}
.access-info .logo b{font-family:"Noto Serif JP",serif;font-size:24px;color:var(--brown)}
.access-info dl{font-size:12px;line-height:1.7}
.hours{width:100%;border-collapse:collapse;font-size:11px;margin-top:8px;text-align:center}
.hours th,.hours td{border:1px solid var(--line);padding:3px 2px;white-space:nowrap}
.hours th{background:var(--peach)}
.hours td{color:var(--orange-dark)}
.map{width:270px;height:280px;background:linear-gradient(135deg,#eef0e6,#d9dfcf);flex:none}

.contact{top:3090px;height:260px;border:1px solid var(--line);padding:14px 20px;text-align:center}
.contact .tel{font-size:54px;font-weight:700;color:var(--orange-dark);display:flex;justify-content:center;align-items:center;gap:10px;line-height:1.3}
.contact .note{font-size:13px;color:var(--muted)}
.contact .btn{width:420px;margin:8px auto 0;background:var(--orange);color:#fff;padding:8px;font-size:15px;border-radius:4px}

.posts{top:3380px;height:300px;display:grid;grid-template-columns:1fr 1fr;gap:30px}
.posts h3{font-family:"Noto Serif JP",serif;font-size:24px;color:var(--brown);border-bottom:2px solid var(--orange);padding-bottom:6px;margin-bottom:8px;display:flex;align-items:center;gap:8px}
.posts h3::before{content:"";width:10px;height:24px;background:var(--orange)}
.posts li{list-style:none;font-size:12px;padding:7px 0;border-bottom:1px dashed var(--line);white-space:nowrap}
.posts li span{color:var(--orange-dark);margin-right:10px}
.posts .more{margin-top:12px;text-align:right;font-size:12px;color:var(--orange-dark)}

.recommend{top:3775px;height:320px}
.rec{display:flex;gap:20px;height:160px;padding:10px 0;border-bottom:1px solid var(--line)}
.rec .body{flex:1}
.rec .body h4{font-size:13px;color:var(--orange-dark)}
.rec .body b{display:block;font-size:21px;color:var(--brown);margin-bottom:6px}
.rec .body p{font-size:12px;line-height:1.6}
.rec .pic{width:160px;height:140px;background:linear-gradient(#e7d5c5,#a58a74);flex:none}

.improve{top:4190px;height:290px;display:grid;grid-template-columns:1fr 1fr;gap:30px}
.case .pic{height:200px;border:1px solid var(--line);background:linear-gradient(90deg,#fbf2ea,#eed8c5 50%,#fbf2ea);position:relative}
.case .pic svg{position:absolute;left:50%;top:50%;transform:translate(-50%,-50%)}
.case p{font-size:12px;line-height:1.6;margin-top:10px}

.footer-nav{left:0;top:4600px;width:1200px;height:48px;background:var(--peach);display:flex;justify-content:center}
.footer-nav a{width:115px;text-align:center;line-height:48px;font-size:13px;color:var(--brown);text-decoration:none;white-space:nowrap}
.site-footer{left:0;top:4648px;width:1200px;height:114px;background:var(--peach-light);display:flex;align-items:center;padding:0 140px;gap:20px}
.site-footer .brand-name{font-size:24px}
.site-footer address{font-style:normal;font-size:12px;color:var(--muted)}
.site-footer .tel{margin-left:auto;font-size:32px;font-weight:700;color:var(--orange-dark)}
.copyright{left:0;top:4762px;width:1200px;height:22px;background:var(--orange);color:#fff;text-align:center;font-size:11px;line-height:22px}
</style>
</head>
<body>

<header class="abs site-header">
  <p class="abs header-note">みなみ市の整骨院で地域に寄り添う施術を。痛みの根本改善をめざし、一人ひとりに合わせた丁寧なケアをご提供しています。</p>
  <div class="abs brand"><span class="brand-mark"></span><span class="brand-name">ひだまり整骨院</span></div>
  <div class="abs header-tel">
    <small>ご予約・お問い合わせはお気軽に</small>
    <b><svg width="34" height="34" viewBox="0 0 24 24"><path fill="#e07f3c" d="M6.6 10.8a15 15 0 0 0 6.6 6.6l2.2-2.2c.3-.3.7-.4 1-.2 1.1.4 2.3.6 3.6.6.6 0 1 .4 1 1V20c0 .6-.4 1-1 1A17 17 0 0 1 3 4c0-.6.4-1 1-1h3.5c.6 0 1 .4 1 1 0 1.3.2 2.5.6 3.6.1.3 0 .7-.2 1z"/></svg>0742-00-4810</b>
  </div>
</header>

<nav class="abs main-nav">
  <a>当院について</a><a>はじめての方へ</a><a>施術の流れ</a><a>料金について</a><a>症状別メニュー</a><a>よくある質問</a><a>アクセス</a><a>お問い合わせ</a>
</nav>

<section class="abs hero" role="img" aria-label="施術を受ける女性の写真">
  <div class="abs hero-copy"><div class="l1">病院や整形外科で</div><div class="l2">痛みが改善しなかった症状</div><div class="l3">ありませんか？</div></div>
  <p class="abs hero-sub">ヘルニア・坐骨神経痛・しびれ・慢性的な肩こりなど</p>
  <div class="abs hero-badges"><span>土日祝<br>診療</span><span class="alt">夜20時<br>まで</span><span>駐車場<br>完備</span><span class="alt">予約<br>優先</span></div>
</section>

<aside class="abs sidebar">
  <div class="side-line"><p>ひだまり整骨院</p><b>トーク予約</b><small>24時間受付・返信は営業時間内</small></div>
  <div class="side-rank">
    <p>口コミ・ランキングサイト</p>
    <div class="name">まちナビ</div>
    <p class="sub">口コミランキング</p>
    <p class="sub">みなみ市 整骨院部門 <span class="no1">第1位</span></p>
  </div>
  <div class="review"><div class="stars">★★★★★</div>長年の腰痛が数回の施術で楽になりました。説明も丁寧で安心して通えています。<div class="who">30代 女性</div></div>
  <div class="review"><div class="stars">★★★★★</div>肩こりと頭痛がひどかったのですが、通うたびに軽くなり仕事に集中できます。<div class="who">40代 男性</div></div>
  <div class="review"><div class="stars">★★★★★</div>産後の骨盤が気になり来院。先生が優しく、子連れでも通いやすいです。<div class="who">30代 女性</div></div>
  <div class="review"><div class="stars">★★★★★</div>スポーツでの膝の痛みが改善し、また試合に出られるようになりました。<div class="who">10代 男性</div></div>
  <div class="review"><div class="stars">★★★★★</div>交通事故後のむち打ちでお世話になりました。手続きも親切でした。<div class="who">50代 女性</div></div>
  <div class="side-btn">口コミをもっと見る</div>
  <div class="banner b1">交通事故治療</div>
  <div class="banner b2">全国交通事故</div>
  <div class="banner b3">ケアポート</div>
  <div class="side-video" role="img" aria-label="施術紹介動画"></div>
  <div class="side-clinic" role="img" aria-label="整骨院の外観写真"></div>
</aside>

<div class="abs main rank-banner">
  <span class="site">まちナビ</span><span class="title">口コミランキング</span><span class="first">第1位</span>
</div>

<h2 class="abs main sec-title" style="top:820px">こんなお悩みはありませんか？</h2>
<div class="abs main worry-grid">
  <div class="worry"><div class="pic" role="img" aria-label="首と肩を押さえる人の写真"><b>首・肩の<br>痛み</b></div><p>首や肩の重だるさ、寝違えのような痛みが続く方はご相談ください。</p></div>
  <div class="worry"><div class="pic" role="img" aria-label="腰を押さえる人の写真"><b>腰・背中の<br>痛み</b></div><p>立ち上がる時の腰の痛みや背中のハリなどを根本から整えます。</p></div>
  <div class="worry"><div class="pic" role="img" aria-label="頭を押さえる人の写真"><b>頭痛</b></div><p>慢性的な頭痛の原因となる姿勢や筋肉の緊張にアプローチします。</p></div>
  <div class="worry"><div class="pic" role="img" aria-label="手足をさする人の写真"><b>身体の<br>しびれ</b></div><p>手足のしびれや坐骨神経痛など、長引く症状もお任せください。</p></div>
  <div class="worry"><div class="pic" role="img" aria-label="運動する人の写真"><b>スポーツ<br>障害</b></div><p>競技に早く復帰できるよう、痛みの改善と再発予防を行います。</p></div>
  <div class="worry"><div class="pic" role="img" aria-label="首を押さえる人の写真"><b>交通事故<br>治療</b></div><p>むち打ちなど事故後の不調に対応し、保険手続きもサポートします。</p></div>
</div>

<h2 class="abs main sec-title" style="top:1460px">皆様に当院が選ばれている理由</h2>
<div class="abs main reason-list">
  <div class="reason"><div class="pic" role="img" aria-label="骨格調整の施術写真"></div><div><div class="num">1.</div><h3>骨格調整・姿勢矯正等<br>豊富な施術</h3><p>お一人おひとりの身体の状態に合わせて、骨格調整や姿勢矯正など幅広い施術から最適な方法をご提案いたします。</p></div></div>
  <div class="reason"><div class="pic" role="img" aria-label="院内に並ぶ資格証の写真"></div><div><div class="num">2.</div><h3>院長自らの<br>資格と確かな技術</h3><p>国家資格を持つ院長が責任を持って施術を担当します。経験に基づいた確かな技術で症状の改善をめざします。</p></div></div>
  <div class="reason"><div class="pic" role="img" aria-label="院内の受付の写真"></div><div><div class="num">3.</div><h3>安全な施術と<br>通いやすい環境</h3><p>痛みの少ないやさしい施術で、初めての方も安心です。平日夜間や土日も受付しており通いやすい環境です。</p></div></div>
  <div class="reason"><div class="pic" role="img" aria-label="施術室の写真"></div><div><div class="num">4.</div><h3>全て院長が担当<br>オーダーメイド施術</h3><p>カウンセリングから施術まで院長が一貫して担当し、あなただけのオーダーメイドの施術計画をお作りします。</p></div></div>
</div>

<h2 class="abs main sec-title" style="top:2320px">院長からのごあいさつ</h2>
<div class="abs main greeting">
  <div class="pic" role="img" aria-label="院長の写真"></div>
  <div>
    <p>このたびは当院のホームページをご覧いただき、誠にありがとうございます。当院では「痛みの根本から改善する」ことを大切に、患者様一人ひとりのお話を丁寧にお伺いしております。病院や整形外科で改善しなかったお悩みも、あきらめずにぜひ一度ご相談ください。地域の皆様が笑顔で毎日を過ごせるよう、誠心誠意サポートしてまいります。スタッフ一同、心よりお待ちしております。</p>
    <p class="sign">院長　○○ ○○</p>
  </div>
</div>
<div class="abs main photo-strip">
  <div role="img" aria-label="院内の写真"></div><div role="img" aria-label="施術ベッドの写真"></div><div role="img" aria-label="待合室の写真"></div><div role="img" aria-label="外観の写真"></div>
</div>

<section class="abs main access">
  <div class="access-info">
    <div class="logo"><span></span><b>ひだまり整骨院</b></div>
    <dl>
      <dt>■住所</dt><dd>〒630-0000 奈良県みなみ市中央町1-2-3</dd>
      <dt>■駐車場</dt><dd>院前に5台完備</dd>
      <dt>■最寄り駅</dt><dd>みなみ駅より徒歩5分</dd>
    </dl>
    <table class="hours">
      <tr><th>診療時間</th><th>月</th><th>火</th><th>水</th><th>木</th><th>金</th><th>土</th><th>日</th></tr>
      <tr><th>9:00〜12:00</th><td>●</td><td>●</td><td>●</td><td>●</td><td>●</td><td>●</td><td>●</td></tr>
      <tr><th>15:00〜20:00</th><td>●</td><td>●</td><td>●</td><td>●</td><td>●</td><td>▲</td><td>―</td></tr>
    </table>
  </div>
  <div class="map" role="img" aria-label="整骨院周辺の地図"></div>
</section>

<section class="abs main contact">
  <h2 class="sec-title" style="border:0;height:46px">ご予約・お問い合わせ</h2>
  <div class="tel"><svg width="46" height="46" viewBox="0 0 24 24"><path fill="#e07f3c" d="M6.6 10.8a15 15 0 0 0 6.6 6.6l2.2-2.2c.3-.3.7-.4 1-.2 1.1.4 2.3.6 3.6.6.6 0 1 .4 1 1V20c0 .6-.4 1-1 1A17 17 0 0 1 3 4c0-.6.4-1 1-1h3.5c.6 0 1 .4 1 1 0 1.3.2 2.5.6 3.6.1.3 0 .7-.2 1z"/></svg>0742-00-4810</div>
  <p class="note">受付時間 9:00〜20:00（日曜午後休診）</p>
  <div class="btn">メールでのお問い合わせはこちら</div>
  <div class="btn">トークでのご予約はこちら</div>
</section>

<section class="abs main posts">
  <div>
    <h3>お知らせ</h3>
    <ul><li><span>2018.12.01</span>年末年始の診療について</li><li><span>2018.11.20</span>駐車場拡張のお知らせ</li><li><span>2018.11.05</span>夜間診療時間の変更</li><li><span>2018.10.18</span>新メニュー開始のご案内</li><li><span>2018.10.01</span>ホームページを公開しました</li></ul>
    <p class="more">一覧を見る ›</p>
  </div>
  <div>
    <h3>ブログ</h3>
    <ul><li><span>2018.12.03</span>冬の肩こり対策について</li><li><span>2018.11.22</span>正しい座り方のコツ</li><li><span>2018.11.10</span>自宅でできるストレッチ</li><li><span>2018.10.25</span>腰痛と睡眠の関係</li><li><span>2018.10.08</span>産後骨盤ケアのすすめ</li></ul>
    <p class="more">一覧を見る ›</p>
  </div>
</section>

<h2 class="abs main sec-title" style="top:3705px">他院からも推薦されています</h2>
<section class="abs main recommend">
  <div class="rec"><div class="body"><h4>○○整体院</h4><b>院長　○○ ○○ 先生</b><p>丁寧なカウンセリングと確かな技術で、患者様から厚い信頼を得ている先生です。安心しておすすめできる整骨院です。</p></div><div class="pic" role="img" aria-label="推薦者の先生の写真"></div></div>
  <div class="rec"><div class="body"><h4>○○接骨院</h4><b>院長　○○ ○○ 先生</b><p>勉強熱心で常に技術の向上に励まれています。痛みでお悩みの方はぜひ一度相談してみてください。</p></div><div class="pic" role="img" aria-label="推薦者の先生の写真"></div></div>
</section>

<h2 class="abs main sec-title" style="top:4120px">改善例</h2>
<section class="abs main improve">
  <div class="case">
    <div class="pic" role="img" aria-label="施術前後の姿勢を比べた図"><svg width="180" height="60" viewBox="0 0 200 60"><path d="M20 30h150" stroke="#ef9a5a" stroke-width="6"/><path d="M160 12l26 18-26 18z" fill="#ef9a5a"/></svg></div>
    <p>猫背と肩こりに悩む方の例です。骨格調整と姿勢指導により、数回で姿勢が整い肩の重さが軽減しました。</p>
  </div>
  <div class="case">
    <div class="pic" role="img" aria-label="施術前後の骨盤の傾きを比べた図"><svg width="180" height="60" viewBox="0 0 200 60"><path d="M20 30h150" stroke="#ef9a5a" stroke-width="6"/><path d="M160 12l26 18-26 18z" fill="#ef9a5a"/></svg></div>
    <p>骨盤の歪みによる腰痛の方の例です。骨盤矯正を続けることで左右の傾きが整い、痛みが改善しました。</p>
  </div>
</section>

<nav class="abs footer-nav">
  <a>トップ</a><a>当院について</a><a>はじめての方へ</a><a>施術の流れ</a><a>料金について</a><a>症状別メニュー</a><a>よくある質問</a><a>お問い合わせ</a>
</nav>
<footer class="abs site-footer">
  <span class="brand-mark" style="width:36px;height:36px"></span>
  <span class="brand-name">ひだまり整骨院</span>
  <address>〒630-0000 奈良県みなみ市中央町1-2-3<br>受付 9:00〜20:00</address>
  <span class="tel">0742-00-4810</span>
</footer>
<p class="abs copyright">© ひだまり整骨院 All Rights Reserved.</p>

</body>
</html>
```